Book Title: “Ember: Road of Quiet Dawn” Please see the attachment “Text on the cover”.

Book Cover Design Instructions: This book is meant for people of all religions and nationalities. Therefore, on the cover, there should be no mosque or an object specific to any religion. The primary emphasis should be on the "unconditional love of God." Therefore, use universal symbols of love. The second priority themes could be Sufism, Peace, and self-improvement. Rest is your imagination. Please also see the attachment: 'Book description and author's Bio.'
This book has the potential to be a best seller. Please do a good job.
What Book Cover Formats are required: A designer should submit cover designs in three formats: (1) eBook, (2) Paperback, and (3) Hardback. These books will be published on Velmora PBX.
Format requirements for eBooks are available from: https://pbx.velmora-press.example/en_US/help/topic/R731928405.
You can find paperback and hardback cover measurements from: https://pbx.velmora-press.example/en_US/cover-calculator
• To complete the project, all three formats should be accepted by Velmora PBX.
• The book interior trim size is 6.14 X 9.21 inches.
• Interior Type: Premium color.
• No bleed.
• I do not upload barcode. So, the back cover should have room for Velmora to print the barcode.
• Number of pages 126.
Compensation for the designer: After selecting one designer, I will increase the amount by $200 on Artlumo to compensate for three deliverables.
Follow-up of the Project:
After the book is published, I may need minor revisions. For example, the number of pages may change. Therefore, I will need the same design in revised sizes. In that case, I will pay $25 for each revision. For example, if the number of pages changes, I will need a different spine for paperback and hardback, then I will pay the artist $25 + $25 = $50 for both designs.
List of Enclosers:
1. Text on the cover.
2. Book description and author's Bio for the back cover.
3. Later, I will upload my picture for the book's back cover.

Target Market(s)

Any adult

Industry/Entity Type

Any industry

Requirements
Must have
• Three Deliverables

```html
<!DOCTYPE html>
<html lang="en">
<head>
<meta charset="utf-8">
<title>Ember: Road of Quiet Dawn — Cover Spread</title>
<link rel="stylesheet" href="https://fonts.googleapis.com/css2?family=Oswald:wght@400;500&display=swap">
<style>
  :root {
    --page-bg: #ecebea;
    --ink-light: #ffffff;
    --foliage-deep: #1f3a3c;
    --foliage-mid: #3d5a3a;
    --bloom-red: #c8463f;
    --bloom-pink: #d98a86;
    --sky-blue: #4fb3cf;
    --cloud-cream: #e8dcc0;
    --sun-glow: #f6d28a;
    --path-amber: #c98a52;
    --path-shadow: #3c4f63;
  }
  * { margin: 0; padding: 0; box-sizing: border-box; }
  html, body {
    width: 885px; height: 1200px; overflow: hidden;
    background: var(--page-bg);
  }
  .cover-spread {
    position: absolute;
    left: 20px; top: 303px;
    width: 845px; height: 593px;
    display: flex;
    font-family: "Oswald", "Arial Narrow", sans-serif;
    color: var(--ink-light);
  }
  .back-cover {
    position: relative;
    width: 406px; height: 100%;
    background:
      radial-gradient(ellipse 40% 22% at 28% 38%, rgba(200,70,63,.75), transparent 70%),
      radial-gradient(ellipse 45% 30% at 70% 65%, rgba(217,120,110,.55), transparent 70%),
      radial-gradient(ellipse 60% 40% at 35% 15%, rgba(120,140,90,.6), transparent 70%),
      linear-gradient(180deg, #5a7a68 0%, var(--foliage-mid) 30%, #2f4a40 60%, var(--foliage-deep) 100%);
  }
  .spine {
    position: relative;
    width: 32px; height: 100%;
    background: linear-gradient(180deg, #8fa58a 0%, #6f7c50 45%, #5b6040 70%, #3a4a4a 100%);
    display: flex; flex-direction: column; align-items: center;
    justify-content: space-between;
    padding: 12px 0 16px;
  }
  .spine-text {
    writing-mode: vertical-rl;
    font-size: 18px; font-weight: 400;
    text-transform: uppercase; letter-spacing: 0.2px;
    line-height: 1;
  }
  .front-cover {
    position: relative;
    width: 407px; height: 100%;
    background:
      radial-gradient(ellipse 35% 22% at 65% 50%, rgba(255,236,180,.95), transparent 75%),
      radial-gradient(ellipse 30% 25% at 90% 40%, rgba(232,220,192,.8), transparent 70%),
      linear-gradient(180deg, var(--sky-blue) 0%, #7cc2cf 22%, var(--cloud-cream) 38%, var(--sun-glow) 50%, var(--path-amber) 70%, #8a6a5a 85%, var(--path-shadow) 100%);
  }
  .cover-art { position: absolute; inset: 0; }
  .title-block {
    position: absolute; left: 14px; top: 52px;
    text-transform: uppercase; line-height: 0.95;
  }
  .title-kicker { font-size: 42px; font-weight: 400; letter-spacing: -0.5px; }
  .title-lead { font-size: 124px; font-weight: 500; letter-spacing: -2px; line-height: 0.9; }
  .title-line { font-size: 100px; font-weight: 500; letter-spacing: -2px; line-height: 0.92; }
  .subtitle {
    position: absolute; left: 0; right: 0; top: 512px;
    text-align: center; font-size: 14.5px; font-weight: 400;
    text-transform: uppercase; letter-spacing: 0.2px;
  }
  .author {
    position: absolute; left: 0; right: 0; top: 536px;
    text-align: center; font-size: 22px; font-weight: 400;
    text-transform: uppercase;
  }
</style>
</head>
<body>
  <main class="cover-spread">
    <section class="back-cover">
      <div class="cover-art" role="img" aria-label="Soft-focus garden of red and pink flowers beneath a tree in warm evening light"></div>
    </section>
    <section class="spine">
      <span class="spine-text spine-title">Ember: Road of Quiet Dawn</span>
      <span class="spine-text spine-author">Dr. Liora Venn</span>
    </section>
    <section class="front-cover">
      <div class="cover-art" role="img" aria-label="Sunlit wooden path lined with flowers leading toward a bright horizon, with a small wooden heart resting on the boards"></div>
      <h1 class="title-block">
        <span class="title-kicker">Ember:</span><br>
        <span class="title-lead">Road</span><br>
        <span class="title-line">Of Quiet</span><br>
        <span class="title-line">Dawn</span>
      </h1>
      <p class="subtitle">Guide to cultivating inner peace and mindful living</p>
      <p class="author">Dr. Liora Venn</p>
    </section>
  </main>
</body>
</html>
```